Business Stationary, Letterhead, Fax Cover Sheet, Client Intake, Email Signature, Thank you cards.
Marwick Law Firm
Business Stationary, Letterhead, Fax Cover Sheet, Client Intake, Email Signature, Thank you cards. - Law
Creative Brief
Professional
Len Marwick
Lawyer
2837 Falbrook St., Suite 1940 Houston, Texas 77014
len@marwick-law.example
www.marwick-law.example
Please note this project is Not for just One Person but for All Staff. The files should be in editable format to allow for different names and titles on cards.

```html
<!DOCTYPE html>
<html lang="en">
<head>
<meta charset="utf-8">
<title>Marwick Law Firm – Business Cards</title>
<link href="https://fonts.googleapis.com/css2?family=Arimo:wght@400;700&display=swap" rel="stylesheet">
<style>
  :root {
    --stage: #4a423b;
    --card-white: #ffffff;
    --card-white-shade: #e4e6e8;
    --card-black: #1c1b1d;
    --card-black-shade: #2c2a2e;
    --blue-deep: #050a3a;
    --blue-bright: #1f45d8;
    --brand-blue: #2a8fd0;
    --ink-dark: #1a1a1a;
    --ink-light: #f2f2f2;
    --rule-blue: #2a3fd0;
  }
  * { margin: 0; padding: 0; box-sizing: border-box; }
  html, body { width: 1200px; height: 851px; overflow: hidden; }
  body {
    background: var(--stage);
    font-family: "Arimo", Arial, sans-serif;
    position: relative;
  }
  .card {
    position: absolute;
    width: 420px;
    height: 255px;
    border-radius: 14px;
    overflow: hidden;
  }
  .card--front-light { left: 156px; top: 100px; background: linear-gradient(160deg, var(--card-white) 40%, var(--card-white-shade)); }
  .card--front-dark  { left: 624px; top: 100px; background: linear-gradient(160deg, var(--card-black-shade), var(--card-black) 60%); color: var(--ink-light); }
  .card--back-blue   { left: 156px; top: 400px; background: radial-gradient(ellipse at 50% 45%, var(--blue-bright), var(--blue-deep) 70%); }
  .card--back-light  { left: 624px; top: 400px; background: linear-gradient(160deg, var(--card-white) 40%, var(--card-white-shade)); }

  .brand {
    position: absolute;
    display: flex;
    flex-direction: column;
    align-items: center;
    gap: 10px;
    font-weight: 700;
    color: var(--brand-blue);
    text-align: center;
    line-height: 1.15;
  }
  .brand__dot { width: 26px; height: 26px; border-radius: 50%; background: var(--brand-blue); }
  .brand--side { left: 22px; top: 58px; width: 130px; font-size: 19px; }
  .brand--center { left: 0; right: 0; top: 70px; font-size: 30px; }
  .card--back-blue .brand { color: #7cc4f0; }
  .card--back-blue .brand__dot { background: #7cc4f0; }

  .divider {
    position: absolute;
    left: 170px; top: 28px;
    width: 2px; height: 125px;
    background: var(--rule-blue);
  }
  .card--front-dark .divider { display: none; }

  .contact {
    position: absolute;
    left: 190px; top: 34px;
    font-size: 11.5px;
    line-height: 1.32;
    color: var(--ink-dark);
  }
  .card--front-dark .contact { color: var(--ink-light); left: 196px; }
  .contact__name { font-weight: 700; font-size: 14px; }
  .contact__title { font-size: 12.5px; margin-bottom: 24px; }

  .web {
    position: absolute;
    left: 0; right: 0; bottom: 14px;
    text-align: center;
    font-size: 11.5px;
    letter-spacing: 2.5px;
    color: var(--ink-dark);
  }
  .card--front-dark .web { color: var(--ink-light); }
</style>
</head>
<body>

  <section class="card card--front-light">
    <div class="brand brand--side"><span class="brand__dot"></span>Marwick Law Firm</div>
    <div class="divider"></div>
    <div class="contact">
      <p class="contact__name">Len Marwick</p>
      <p class="contact__title">Lawyer</p>
      <p>2837 Falbrook St., Suite 1940</p>
      <p>Houston, Texas 77014</p>
      <p>Phone : 713-555-0148</p>
      <p>Fax&nbsp;&nbsp;&nbsp;: 713-555-0148</p>
      <p>Email : len@marwick-law.example</p>
    </div>
    <p class="web">www.marwick-law.example</p>
  </section>

  <section class="card card--front-dark">
    <div class="brand brand--side"><span class="brand__dot"></span>Marwick Law Firm</div>
    <div class="divider"></div>
    <div class="contact">
      <p class="contact__name">Len Marwick</p>
      <p class="contact__title">Lawyer</p>
      <p>2837 Falbrook St., Suite 1940</p>
      <p>Houston, Texas 77014</p>
      <p>Phone : 713-555-0148</p>
      <p>Fax&nbsp;&nbsp;&nbsp;: 713-555-0148</p>
      <p>Email : len@marwick-law.example</p>
    </div>
    <p class="web">www.marwick-law.example</p>
  </section>

  <section class="card card--back-blue">
    <div class="brand brand--center"><span class="brand__dot"></span>Marwick Law Firm</div>
  </section>

  <section class="card card--back-light">
    <div class="brand brand--center"><span class="brand__dot"></span>Marwick Law Firm</div>
  </section>

</body>
</html>
```